Embrace New Horizons (Postcard)

Looking for a professional post card (5x7) - front and back, graphic design to promote a campaign called Embrace New Horizons. The goal is to promote Orthodontics in our dental practice for our existing and new patients.

```html
<!DOCTYPE html>
<html lang="en">
<head>
<meta charset="UTF-8">
<title>Embrace New Horizons Postcard</title>
<link rel="stylesheet" href="https://fonts.googleapis.com/css2?family=Outfit:wght@300;400;500;800&family=Barlow+Condensed:wght@700&display=swap">
<style>
  :root {
    --navy: #1f3f8a;
    --orange: #e4701f;
    --band: #e6e7e9;
    --ink: #2f2f33;
    --paper: #ffffff;
    --backdrop: #efefef;
    --photo-warm-a: #c9a27e;
    --photo-warm-b: #d9559e;
    --photo-team-a: #2a3a66;
    --photo-team-b: #8a8fa3;
  }
  * { margin: 0; padding: 0; box-sizing: border-box; }
  html, body { width: 1200px; height: 789px; overflow: hidden; }
  body {
    background: var(--backdrop);
    font-family: "Outfit", sans-serif;
    color: var(--ink);
    position: relative;
  }
  .postcard {
    position: absolute;
    top: 117px;
    width: 396px;
    height: 555px;
    background: var(--paper);
    overflow: hidden;
  }
  .postcard--front { left: 138px; }
  .postcard--back { left: 666px; }

  .brand {
    position: absolute;
    left: 0; right: 0;
    display: flex;
    justify-content: center;
    align-items: center;
    gap: 8px;
    color: var(--navy);
    font-weight: 500;
    white-space: nowrap;
  }
  .brand__dot { border-radius: 50%; background: var(--orange); flex: none; }
  .postcard--front .brand { top: 48px; font-size: 25px; }
  .postcard--front .brand__dot { width: 22px; height: 22px; }
  .postcard--back .brand { top: 54px; font-size: 17px; }
  .postcard--back .brand__dot { width: 14px; height: 14px; }

  .photo { position: absolute; left: 0; width: 100%; }
  .photo--family {
    top: 91px; height: 331px;
    background: linear-gradient(120deg, #a9b98a 0%, var(--photo-warm-a) 45%, var(--photo-warm-b) 100%);
  }
  .photo--team {
    top: 357px; height: 164px;
    background: linear-gradient(180deg, var(--photo-team-b) 0%, var(--photo-team-a) 55%, #1d2b52 100%);
  }

  .band { position: absolute; left: 0; width: 100%; background: var(--band); }
  .postcard--front .band { top: 422px; height: 99px; }
  .postcard--back .band { top: 239px; height: 118px; }

  .footer {
    position: absolute;
    left: 0; bottom: 0;
    width: 100%; height: 34px;
    background: var(--navy);
    color: var(--paper);
    font-size: 11px;
    letter-spacing: 2.6px;
    display: flex; align-items: center; justify-content: center;
  }

  .campaign {
    position: absolute;
    left: 33px; top: 437px;
    font-size: 20px;
    line-height: 19px;
  }
  .campaign span { display: block; }
  .campaign__lead { font-weight: 300; }
  .campaign__accent { color: var(--orange); font-weight: 800; }
  .campaign__name { font-weight: 400; color: var(--ink); }

  .offer { position: absolute; left: 229px; top: 375px; width: 140px; height: 147px; }
  .offer__text {
    position: absolute;
    left: 0; width: 100%;
    text-align: center;
    color: var(--paper);
  }
  .offer__enjoy { top: 18px; color: var(--orange); font-size: 13px; }
  .offer__amount { top: 32px; font-family: "Barlow Condensed", sans-serif; font-weight: 700; font-size: 44px; line-height: 44px; }
  .offer__label { top: 78px; font-size: 10px; line-height: 11px; letter-spacing: 0.3px; }

  .headline {
    position: absolute;
    left: 0; top: 116px; width: 100%;
    text-align: center;
  }
  .headline__intro { font-size: 26px; font-weight: 300; line-height: 34px; display: block; }
  .headline__accent { color: var(--orange); font-weight: 800; display: block; }
  .headline__accent--top { font-size: 30px; line-height: 30px; }
  .headline__accent--big { font-size: 44px; line-height: 40px; }

  .cta {
    position: absolute;
    left: 0; top: 256px; width: 100%;
    text-align: center;
    font-size: 13px; line-height: 15px;
  }
  .phone {
    position: absolute;
    left: 0; top: 290px; width: 100%;
    text-align: center;
    font-family: "Barlow Condensed", sans-serif;
    font-weight: 700;
    font-size: 46px;
    line-height: 50px;
    color: var(--navy);
  }
</style>
</head>
<body>
  <section class="postcard postcard--front">
    <div class="brand"><span class="brand__dot"></span>Brightline Dental</div>
    <div class="photo photo--family" role="img" aria-label="Photo of a smiling mother and young child outdoors"></div>
    <div class="band"></div>
    <p class="campaign">
      <span class="campaign__lead">Embrace</span>
      <span class="campaign__accent">NEW HORIZONS</span>
      <span><span class="campaign__accent" style="display:inline">WITH</span> <span class="campaign__name" style="display:inline">Brightline Dental</span></span>
    </p>
    <div class="offer">
      <svg width="140" height="147" viewBox="0 0 140 147" aria-hidden="true">
        <defs><clipPath id="offer-clip"><rect x="0" y="0" width="140" height="125"/></clipPath></defs>
        <g clip-path="url(#offer-clip)">
          <circle cx="70" cy="70" r="70" fill="#e6e7e9"/>
          <circle cx="70" cy="70" r="63" fill="#1f3f8a"/>
        </g>
      </svg>
      <span class="offer__text offer__enjoy">Enjoy</span>
      <span class="offer__text offer__amount">$500</span>
      <span class="offer__text offer__label">ORTHODONTIC<br>TREATMENT</span>
    </div>
    <div class="footer">BrightlineDental.com</div>
  </section>

  <section class="postcard postcard--back">
    <div class="brand"><span class="brand__dot"></span>Brightline Dental</div>
    <h1 class="headline">
      <span class="headline__intro">Offering Braces for</span>
      <span class="headline__accent headline__accent--top">YOUR BEST</span>
      <span class="headline__accent headline__accent--big">SMILE!</span>
    </h1>
    <div class="band"></div>
    <p class="cta">Call Today to Schedule Your<br>Appointment or Free Consultation</p>
    <p class="phone">(555) 014-2760</p>
    <div class="photo photo--team" role="img" aria-label="Group photo of the dental practice team in navy uniforms"></div>
    <div class="footer">BrightlineDental.com</div>
  </section>
</body>
</html>
```